Modern Dry eye Poster for eye center, Optometrist office

We need a banner to connect to patient about dry eye and treatment. Ask if patient has dry eyes and we offer treatment .
What is dry eye?
Are you suffering for dry, gritty, painful eyes, blurred vision, redness..

Now there is a quick, comfortable and affordable procedure offering relief tofdry eye.

Schedule your dry eye treatment today.

Target Market(s)

Dry eye patient

Font styles to use
Sans Serif

Colors
00a990
ffffff
0492cd
fbf289
85cae6

Requirements
Must have
• Modern design, dry eye patient
Nice to have
• real life model of nice eyes
Should not have
• No cartoon,

```html
<!DOCTYPE html>
<html lang="en">
<head>
<meta charset="utf-8">
<title>What Is Dry Eye – Lumen Optometry</title>
<link href="https://fonts.googleapis.com/css2?family=Montserrat:wght@300;400;700;800&display=swap" rel="stylesheet">
<style>
  :root {
    --gold: #e2bb2e;
    --blue: #0a8fd0;
    --ink: #1c1c1c;
    --body: #3a3a3a;
    --cream: #fffbea;
    --paper: #ffffff;
    --swoosh: #c9c9c9;
    --brand-grey: #6a6a6a;
  }
  * { margin: 0; padding: 0; box-sizing: border-box; }
  html, body { width: 900px; height: 1200px; overflow: hidden; background: var(--paper); }
  .poster {
    position: relative;
    width: 900px;
    height: 1200px;
    overflow: hidden;
    font-family: "Montserrat", sans-serif;
    background: linear-gradient(180deg, var(--paper) 0%, var(--paper) 45%, var(--cream) 100%);
  }
  .artwork { position: absolute; inset: 0; }
  .headline { position: absolute; right: 36px; top: 26px; text-align: right; }
  .headline__lead {
    display: block; font-weight: 400; font-size: 98px; line-height: 96px;
    color: var(--ink); letter-spacing: -1px;
  }
  .headline__key {
    display: block; font-weight: 800; font-size: 172px; line-height: 134px;
    color: var(--gold); letter-spacing: -4px; margin-right: -6px;
  }
  .rule { position: absolute; right: 44px; width: 100px; height: 2px; background: var(--gold); opacity: .7; }
  .rule--top { top: 412px; }
  .rule--bottom { top: 703px; }
  .symptoms { position: absolute; right: 38px; top: 440px; text-align: right; width: 470px; }
  .symptoms__ask { font-weight: 300; font-size: 27px; line-height: 34px; color: var(--ink); }
  .symptoms__list {
    font-weight: 800; font-size: 30px; line-height: 36px; color: var(--blue);
    margin-top: 3px; letter-spacing: -0.3px;
  }
  .intro {
    position: absolute; right: 36px; top: 726px; width: 540px; text-align: right;
    font-weight: 300; font-size: 20px; line-height: 29px; color: var(--body); letter-spacing: -0.2px;
  }
  .brand { position: absolute; left: 57px; top: 982px; }
  .brand__mark { width: 112px; height: 112px; background: var(--gold); margin-left: 18px; margin-bottom: 44px; }
  .brand__name {
    font-weight: 300; font-size: 28px; line-height: 26px; color: var(--brand-grey); letter-spacing: 1px;
  }
  .cta { position: absolute; right: 28px; top: 1084px; text-align: right; }
  .cta__line { font-weight: 400; font-size: 23px; color: var(--ink); }
  .cta__line strong { font-weight: 700; }
  .cta__rule { width: 70px; height: 2px; background: var(--blue); opacity: .5; margin: 4px 0 0 auto; }
  .cta__phone {
    font-weight: 800; font-size: 70px; line-height: 80px; color: var(--gold); letter-spacing: -2px;
  }
</style>
</head>
<body>
<main class="poster">
  <svg class="artwork" width="900" height="1200" viewBox="0 0 900 1200">
    <defs>
      <linearGradient id="skinBase" x1="0" y1="0" x2="1" y2="0">
        <stop offset="0" stop-color="#e7b596"/>
        <stop offset="0.45" stop-color="#f2d2bc"/>
        <stop offset="0.8" stop-color="#f6e0d0"/>
        <stop offset="1" stop-color="#ffffff" stop-opacity="0"/>
      </linearGradient>
      <radialGradient id="warmUpper" cx="0.42" cy="0.3" r="0.45">
        <stop offset="0" stop-color="#b9875e" stop-opacity="0.55"/>
        <stop offset="1" stop-color="#b9875e" stop-opacity="0"/>
      </radialGradient>
      <radialGradient id="lightCheek" cx="0.35" cy="0.62" r="0.4">
        <stop offset="0" stop-color="#fbeadf" stop-opacity="0.8"/>
        <stop offset="1" stop-color="#fbeadf" stop-opacity="0"/>
      </radialGradient>
      <linearGradient id="hairShade" x1="0" y1="0" x2="1" y2="0">
        <stop offset="0" stop-color="#5a3b28" stop-opacity="0"/>
        <stop offset="0.5" stop-color="#5a3b28" stop-opacity="0.45"/>
        <stop offset="1" stop-color="#5a3b28" stop-opacity="0"/>
      </linearGradient>
      <linearGradient id="fadeDown" x1="0" y1="0" x2="0" y2="1">
        <stop offset="0" stop-color="#ffffff" stop-opacity="1"/>
        <stop offset="0.55" stop-color="#ffffff" stop-opacity="1"/>
        <stop offset="1" stop-color="#ffffff" stop-opacity="0"/>
      </linearGradient>
      <mask id="hairMask">
        <rect x="0" y="0" width="900" height="700" fill="url(#fadeDown)"/>
      </mask>
      <linearGradient id="deviceTone" x1="0" y1="0" x2="1" y2="1">
        <stop offset="0" stop-color="#eef3f8"/>
        <stop offset="0.5" stop-color="#c7d3e0"/>
        <stop offset="1" stop-color="#7f93a8"/>
      </linearGradient>
    </defs>

    <g role="img" aria-label="Close-up photo of a woman's face with cracked, dry skin around one eye">
      <path fill="url(#skinBase)" d="M0 0 H560 V900 C520 960 480 985 440 990 C300 960 150 950 0 977 Z"/>
      <path fill="url(#warmUpper)" d="M0 0 H560 V900 C520 960 480 985 440 990 C300 960 150 950 0 977 Z"/>
      <path fill="url(#lightCheek)" d="M0 0 H560 V900 C520 960 480 985 440 990 C300 960 150 950 0 977 Z"/>
      <rect x="410" y="0" width="90" height="700" fill="url(#hairShade)" mask="url(#hairMask)"/>
    </g>

    <path fill="var(--cream)" d="M0 977 C200 920 430 998 614 1030 C760 1050 850 975 900 928 V1200 H0 Z"/>
    <path class="swoosh" fill="none" stroke="var(--swoosh)" stroke-width="3"
          d="M0 977 C200 920 430 998 614 1030 C760 1050 850 975 900 928"/>
    <circle cx="696" cy="977" r="94" fill="#ffffff" stroke="#d5d5d5" stroke-width="4"/>
    <circle role="img" aria-label="Photo of the dry eye treatment device" cx="696" cy="977" r="87" fill="url(#deviceTone)"/>
  </svg>

  <h1 class="headline">
    <span class="headline__lead">WHAT IS</span>
    <span class="headline__key">DRY</span>
    <span class="headline__key">EYE</span>
  </h1>

  <div class="rule rule--top"></div>

  <section class="symptoms">
    <p class="symptoms__ask">ARE YOU SUFFERING FROM</p>
    <p class="symptoms__list">DRY EYE SENSATION,<br>SCRATCH, BURNING,<br>STINGING, ITCHING, EXCES-<br>SIVE TEARING, CONTACT<br>LENS DISCOMFORT,<br>SORENESS?</p>
  </section>

  <div class="rule rule--bottom"></div>

  <p class="intro">Now there is a quick, comfortable and affordable<br>procedure offering relief to dry eye. We have a<br>quick, comfortable and affordable<br>procedureoffering dry eye relief.</p>

  <div class="brand">
    <div class="brand__mark"></div>
    <p class="brand__name">LUMEN<br>OPTOMETRY</p>
  </div>

  <div class="cta">
    <p class="cta__line">Schedule Your <strong>DRY EYE</strong> Treatment <strong>Today</strong></p>
    <div class="cta__rule"></div>
    <p class="cta__phone">555.214.7730</p>
  </div>
</main>
</body>
</html>
```